Business Card Design For Marketing Agnecy LVT

Need business card design for marketing agency.

Dorian Pell
President, CEO
1-555-304-2917
dorian@lumenvaletrewards.net
www.LumenValeTrewards.biz

Back Side:
Boost Sales Using Rewards, Incentives & Giveaways
Get A Free Sample Package

Target Market(s)

B2B

Industry/Entity Type

Marketing

Contact Information for Business Card

Dorian Pell
President, CEO
1-555-304-2917

Back Side:
Get A Free Sample Package

Please note that my current url is OLD DESIGN. I am working on new design and want the business card to match color themes at least on new site. Here is the demo link for new site so you can see the colors I use, etc.

http://pagekilnstudio.example/qx/dorian/lvt_final/index.html

Requirements
Must have
• Please note that my current url is OLD DESIGN. I am working on new design and want the business card to match color themes at least on new site. Here is the demo link for new site so you can see the colors I use, etc.

Nice to have

Should not have

```html
<!DOCTYPE html>
<html lang="en">
<head>
<meta charset="utf-8">
<title>LVT Business Card – Front and Back</title>
<link rel="stylesheet" href="https://fonts.googleapis.com/css2?family=Poppins:wght@300;400;600;700;800&display=swap">
<style>
  :root {
    --stage: #97a0b3;
    --brand-blue: #1b6fbd;
    --ink: #111111;
    --photo-dark: #1f1f21;
    --paper: #f3f3f3;
    --muted-mark: #c4c4c4;
    --white: #ffffff;
    --soft-white: #d9d9d9;
  }
  * { box-sizing: border-box; margin: 0; padding: 0; }
  html, body {
    width: 1200px; height: 800px; overflow: hidden;
    background: var(--stage);
    font-family: "Poppins", sans-serif;
  }
  .canvas {
    width: 1200px; height: 800px;
    display: flex; align-items: center; justify-content: center; gap: 40px;
  }
  .card {
    position: relative;
    width: 540px; height: 309px;
    overflow: hidden;
    box-shadow: 0 18px 40px rgba(30, 36, 52, 0.35);
  }
  .card-art { position: absolute; inset: 0; width: 100%; height: 100%; }

  /* Front */
  .card-front { background: var(--photo-dark); }
  .contact-name {
    position: absolute; left: 222px; top: 32px;
    font-size: 25px; line-height: 1; color: var(--ink); letter-spacing: -0.5px;
  }
  .contact-name .first { font-weight: 300; }
  .contact-name .last { font-weight: 800; }
  .contact-role {
    position: absolute; left: 222px; top: 62px;
    font-size: 14px; color: var(--ink);
  }
  .contact-role .strong { font-weight: 700; }
  .contact-role .light { font-weight: 300; }
  .contact-list { position: absolute; left: 228px; top: 96px; list-style: none; }
  .contact-item {
    display: flex; align-items: center; gap: 10px;
    height: 30px; margin-bottom: 8px;
    font-size: 12px; font-weight: 400; color: var(--ink);
    white-space: nowrap;
  }
  .contact-item:nth-child(2) { margin-left: 14px; }
  .contact-item:nth-child(3) { margin-left: 28px; }
  .contact-icon {
    width: 26px; height: 26px; border-radius: 50%;
    background: var(--brand-blue);
    display: flex; align-items: center; justify-content: center;
    flex: none;
  }
  .contact-icon svg { width: 14px; height: 14px; }
  .front-brand {
    position: absolute; left: 118px; top: 200px;
    font-size: 56px; font-weight: 700; line-height: 1; color: var(--brand-blue);
    letter-spacing: 1px;
  }
  .corner-brand {
    position: absolute; right: 24px; bottom: 20px;
    font-size: 24px; font-weight: 700; color: var(--muted-mark);
  }

  /* Back */
  .card-back { background: var(--ink); }
  .back-message {
    position: absolute; left: 150px; top: 48px; width: 370px;
    color: var(--white);
  }
  .back-message .headline { font-size: 12px; font-weight: 300; letter-spacing: 0.3px; }
  .back-message .headline strong { font-weight: 700; }
  .back-message .offer { font-size: 13px; font-weight: 700; margin-top: 4px; }
  .back-message .site { font-size: 11px; font-weight: 300; margin-top: 4px; color: var(--soft-white); letter-spacing: 0.4px; }
  .back-brand {
    position: absolute; left: 150px; top: 190px;
    font-size: 48px; font-weight: 700; line-height: 1; color: var(--white);
    letter-spacing: 1px;
  }
</style>
</head>
<body>
<main class="canvas">

  <section class="card card-front" aria-label="Business card front">
    <svg class="card-art" viewBox="0 0 540 309" preserveAspectRatio="none">
      <defs>
        <linearGradient id="officeTone" x1="0" y1="0" x2="1" y2="1">
          <stop offset="0" stop-color="#2e2e31"/>
          <stop offset="1" stop-color="#161617"/>
        </linearGradient>
      </defs>
      <rect width="540" height="309" fill="url(#officeTone)" role="img" aria-label="Dark office interior photograph"/>
      <path d="M0 0 H78 C56 110 58 220 92 309 H0 Z" fill="var(--brand-blue)"/>
      <path d="M192 0 C186 70 192 130 220 168 C240 196 270 210 320 212 L345 205 C330 240 320 275 314 309 H540 V0 Z" fill="var(--paper)"/>
    </svg>

    <h1 class="contact-name"><span class="first">DORIAN</span> <span class="last">PELL</span></h1>
    <p class="contact-role"><span class="strong">President</span><span class="light">, CEO</span></p>

    <ul class="contact-list">
      <li class="contact-item">
        <span class="contact-icon">
          <svg viewBox="0 0 24 24"><path d="M6.6 10.8a15 15 0 0 0 6.6 6.6l2.2-2.2a1 1 0 0 1 1-.25 11.4 11.4 0 0 0 3.6.57 1 1 0 0 1 1 1V20a1 1 0 0 1-1 1A17 17 0 0 1 3 4a1 1 0 0 1 1-1h3.5a1 1 0 0 1 1 1c0 1.25.2 2.45.57 3.6a1 1 0 0 1-.25 1z" fill="#fff"/></svg>
        </span>
        1-555-304-2917
      </li>
      <li class="contact-item">
        <span class="contact-icon">
          <svg viewBox="0 0 24 24"><rect x="3" y="6" width="18" height="13" rx="1.5" fill="#fff"/><path d="M3.5 7 12 13l8.5-6" stroke="var(--brand-blue)" stroke-width="1.6" fill="none"/></svg>
        </span>
        dorian@lumenvaletrewards.net
      </li>
      <li class="contact-item">
        <span class="contact-icon">
          <svg viewBox="0 0 24 24" fill="none" stroke="#fff" stroke-width="1.6"><circle cx="12" cy="12" r="8.5"/><ellipse cx="12" cy="12" rx="3.8" ry="8.5"/><path d="M3.5 12h17M5 7.5h14M5 16.5h14"/></svg>
        </span>
        www.LumenValeTrewards.biz
      </li>
    </ul>

    <p class="front-brand">LVT</p>
    <p class="corner-brand">LVT</p>
  </section>

  <section class="card card-back" aria-label="Business card back">
    <svg class="card-art" viewBox="0 0 540 309" preserveAspectRatio="none">
      <defs>
        <linearGradient id="backTone" x1="0" y1="0" x2="1" y2="1">
          <stop offset="0" stop-color="#1c1c1e"/>
          <stop offset="1" stop-color="#0b0b0c"/>
        </linearGradient>
      </defs>
      <rect width="540" height="309" fill="url(#backTone)" role="img" aria-label="Dark office workspace photograph"/>
      <path d="M0 58 C120 40 260 120 360 309" stroke="var(--brand-blue)" stroke-width="1.6" fill="none"/>
      <path d="M410 0 L540 150" stroke="var(--brand-blue)" stroke-width="1.6" fill="none"/>
    </svg>

    <div class="back-message">
      <p class="headline">BOOST SALES USING REWARDS, <strong>INCENTIVES &amp; GIVEAWAYS</strong></p>
      <p class="offer">GET A FREE SAMPLE PACKAGE</p>
      <p class="site">WWW.LUMENVALETREWARDS.BIZ</p>
    </div>

    <p class="back-brand">LVT</p>
  </section>

</main>
</body>
</html>
```